Boutique hotel requires flyer for Tapas promotion

We need a flyer that will predominantly be used as a Face book promotion and for our website.
We would like to promote the fact that we offer Tapas & open our wine bar from 5pm to 8pm every Friday. Great for after work drinks, parties, corporate events etc.
I have attached our logo that I would like incorporated.
Our website is www.tamberlow.com.au if you would like to get a feel for the property.

Hotel

```html
<!DOCTYPE html>
<html lang="en">
<head>
<meta charset="utf-8">
<title>Tamberlow – Friday Tapas &amp; Wine Bar</title>
<link rel="stylesheet" href="https://fonts.googleapis.com/css2?family=Cinzel:wght@700&family=Playball&family=Playfair+Display:ital,wght@1,400&display=swap">
<style>
  :root {
    --canvas-tan: #c78a45;
    --canvas-tan-deep: #b37434;
    --header-grey: #c9c9c9;
    --header-grey-light: #dcdcdc;
    --wave-line: #f4f4f4;
    --title-red: #a3281c;
    --title-shadow: #1c1c1c;
    --logo-frame: #e39a3c;
    --logo-ink: #8a3b1c;
    --photo-frame: #2a1a10;
    --photo-tone-a: #6e2a14;
    --photo-tone-b: #4a2414;
    --body-ink: #111111;
  }
  * { margin: 0; padding: 0; box-sizing: border-box; }
  html, body { width: 800px; height: 1200px; overflow: hidden; }
  body { background: var(--canvas-tan); }

  .flyer {
    position: relative;
    width: 800px;
    height: 1200px;
    overflow: hidden;
    background: radial-gradient(ellipse at 50% 55%, var(--canvas-tan) 55%, var(--canvas-tan-deep) 100%);
  }

  .header-band {
    position: absolute;
    inset: 0 0 auto 0;
    width: 800px;
    height: 240px;
  }

  .brand-box {
    position: absolute;
    left: 13px;
    top: 24px;
    width: 195px;
    height: 196px;
    background: #ffffff;
    border: 5px solid var(--logo-frame);
    border-radius: 14px;
    display: flex;
    align-items: center;
    justify-content: center;
  }
  .brand-name {
    font-family: "Playfair Display", serif;
    font-style: italic;
    font-weight: 400;
    font-size: 34px;
    color: var(--logo-ink);
  }

  .venue-title {
    position: absolute;
    left: 222px;
    top: 72px;
    width: 560px;
    text-align: center;
    font-family: "Cinzel", serif;
    font-weight: 700;
    font-size: 62px;
    letter-spacing: 4px;
    color: var(--title-red);
    text-shadow: 3px 3px 0 var(--title-shadow), 1px 1px 0 var(--title-shadow);
    white-space: nowrap;
  }

  .feature-photo {
    position: absolute;
    left: 85px;
    top: 336px;
    width: 630px;
    height: 416px;
    border: 4px solid var(--photo-frame);
    box-shadow: 0 6px 16px rgba(0,0,0,0.45);
    background: linear-gradient(160deg, var(--photo-tone-a), var(--photo-tone-b));
  }

  .announcement {
    position: absolute;
    left: 58px;
    top: 768px;
    width: 730px;
    font-family: "Playball", cursive;
    font-size: 62px;
    line-height: 66px;
    color: var(--body-ink);
    white-space: nowrap;
  }
</style>
</head>
<body>
<main class="flyer">
  <svg class="header-band" viewBox="0 0 800 240" aria-hidden="true">
    <defs>
      <linearGradient id="greyFade" x1="0" y1="0" x2="0" y2="1">
        <stop offset="0" stop-color="#dcdcdc"/>
        <stop offset="1" stop-color="#c9c9c9"/>
      </linearGradient>
    </defs>
    <path d="M0,0 H800 V118 C640,118 520,128 420,150 C300,176 180,196 0,186 Z" fill="url(#greyFade)"/>
    <path d="M0,186 C180,196 300,176 420,150 C520,128 640,118 800,118" fill="none" stroke="#f4f4f4" stroke-width="7"/>
  </svg>

  <div class="brand-box">
    <span class="brand-name">Tamberlow</span>
  </div>

  <h1 class="venue-title">TAMBERLOW</h1>

  <div class="feature-photo" role="img" aria-label="Photo of a tapas spread with bread, tomatoes, olive oil, cured meats and a glass and bottle of red wine"></div>

  <p class="announcement">We are happy to annonce that<br>we offer Tapas and open our<br>wine bar from 5pm to 8 pm<br>every Friday.</p>
</main>
</body>
</html>
```